Create Oceanfront SEO Website – Cormant Haven

I am web developer to build a high-quality, SEO-optimized website. The site is fully structured with content, layout, and purpose clearly defined, and comes with keyword-rich SEO guidance to maximize search engine visibility. Domain names and page content are provided.

Developer Role:
Build a responsive, fast-loading website in WordPress, allowing us to edit and update content in the future.
Implement SEO best practices, including meta tags, structured data, and optimized content.
Ensure smooth navigation, intuitive UX, and visually appealing design.
Establish the website to a fully functional state, after which we will handle ongoing updates and changes.
Domain and website will be hosted by hostivel under my profile.
Key Highlights:
Structured website with ready-to-use content.
SEO-focused pages for maximum visibility.
Domains and site structure already defined.
Creative freedom in design within the provided framework.

Target Market(s)

vacationers

Industry/Entity Type

vacation and travel

Coding

Coded - Design and coding required

Colors
0054AA
0677BA
7BADD7
CADEEF
E8F1F8
0094D4
00A9DD
6FCCEA
C7EBF8
E9F6FB
00AB8E
00BBA5
67D7C9
C6EFE9
E9F9F6
FFF300
FFF600
FEFA6F
FFFEC7
FFFEE8

Requirements
Must have
• see brief

```html
<!DOCTYPE html>
<html lang="en">
<head>
<meta charset="utf-8">
<title>Cormant Haven – Oceanfront Condo</title>
<link rel="stylesheet" href="https://fonts.googleapis.com/css2?family=Roboto:wght@400;500;700&family=Lato:wght@400;700&display=swap">
<style>
:root{
  --navy:#0054AA;
  --blue:#0677BA;
  --accent:#1f82c8;
  --sky:#7BADD7;
  --pale-blue:#E4F0FA;
  --mist:#F1F6FB;
  --teal:#00AB8E;
  --mint:#6FCCBF;
  --yellow:#FFF300;
  --ink:#111;
  --text:#333;
  --white:#fff;
  --black:#000;
}
*{box-sizing:border-box;margin:0;padding:0}
html,body{width:1200px;height:4699px;overflow:hidden}
body{position:relative;background:var(--white);font-family:"Lato",sans-serif;color:var(--text)}
.abs{position:absolute}
a{color:inherit;text-decoration:none}

/* top bar */
.topbar{top:0;left:0;width:1200px;height:40px;background:var(--accent);color:var(--white);font:700 14px "Roboto",sans-serif}
.topbar .cta{left:110px;top:12px}
.topbar .social{right:118px;top:12px;display:flex;gap:10px}
.topbar .social span{width:14px;height:14px;border-radius:50%;background:var(--white);display:block}

/* header */
.header{top:40px;left:0;width:1200px;height:86px;background:var(--white)}
.brand{left:110px;top:24px;font:700 29px "Roboto",sans-serif;color:var(--accent)}
.nav{top:32px;font:400 15px "Roboto",sans-serif;color:var(--ink)}
.nav.active{color:var(--accent);text-decoration:underline;text-underline-offset:4px;font-weight:500}
.btn-contact{left:943px;top:24px;width:146px;height:44px;border-radius:22px;background:var(--accent);color:var(--white);font:700 15px "Roboto",sans-serif;display:flex;align-items:center;justify-content:center}

.subnav{top:126px;left:0;width:1200px;height:40px;background:var(--mint);color:var(--white);font:400 15px "Roboto",sans-serif}
.subnav span{position:absolute;top:11px}

/* hero */
.hero{top:166px;left:0;width:1200px;height:591px;overflow:hidden}
.hero-photo{position:absolute;inset:0;background:linear-gradient(180deg,#4f6e86 0%,#7b8f9a 40%,#9a8f80 70%,#6c6358 100%)}
.hero-shade{position:absolute;inset:0;background:rgba(10,30,50,.35)}
.hero svg{position:absolute;left:0;top:0}
.hero h1{position:absolute;left:0;width:1200px;top:112px;text-align:center;color:var(--white);font:700 44px/52px "Roboto",sans-serif}
.hero p{position:absolute;left:0;width:1200px;top:236px;text-align:center;color:var(--white);font:400 16px/27px "Roboto",sans-serif}
.pill{position:absolute;top:310px;height:40px;border-radius:20px;color:var(--white);font:700 14px "Roboto",sans-serif;display:flex;align-items:center;justify-content:center}

/* section titles */
.title{left:0;width:1200px;text-align:center;font:400 35px "Roboto",sans-serif;color:var(--ink)}
.title b{color:var(--accent);font-weight:700}
.rule{left:559px;width:82px;height:3px;background:var(--accent)}

.welcome-text{left:168px;width:864px;top:922px;text-align:center;font:400 15.5px/28px "Roboto",sans-serif;color:var(--ink)}
.bubble{width:294px;height:294px;border-radius:50%;top:1077px;overflow:hidden;border:4px solid var(--white)}
.bubble .label{position:absolute;left:0;width:100%;top:226px;text-align:center;color:var(--white);font:500 19px "Roboto",sans-serif}
.bubble .label svg{vertical-align:-2px;margin-left:6px}

/* why */
.why{top:1487px;left:0;width:1200px;height:640px;background:var(--pale-blue)}
.why-photo{left:111px;top:94px;width:447px;height:453px;border:4px solid var(--white);box-shadow:0 2px 8px rgba(0,0,0,.2);background:linear-gradient(160deg,#7f9a7d 0%,#a9a491 45%,#c7b48f 70%,#5a8fa8 100%)}
.why h2{left:642px;top:72px;font:400 37px/48px "Roboto",sans-serif;color:var(--ink)}
.why h2 b{color:var(--accent);font-weight:700}
.features{left:642px;top:184px;list-style:none;font:400 14px "Lato",sans-serif;color:var(--ink)}
.features li{height:43px;display:flex;align-items:flex-start;gap:12px}
.sq{position:absolute;height:44px;border-radius:5px;color:var(--white);font:400 17px "Lato",sans-serif;display:flex;align-items:center;justify-content:center}

/* explore */
.explore-text{left:166px;width:868px;top:2274px;text-align:center;font:400 15px/25px "Lato",sans-serif;color:var(--text)}
.card{top:2386px;width:308px;height:359px;border:3px solid #e3e3e3;border-radius:6px;background:var(--white)}
.card .shot{position:absolute;left:12px;top:12px;width:278px;height:284px;border-radius:4px}
.card h3{position:absolute;left:0;width:100%;top:320px;text-align:center;font:700 16px "Roboto",sans-serif;color:var(--ink)}

/* testimonials */
.testimonials{top:2847px;left:0;width:1200px;height:595px;background:var(--mist)}
.quote{top:212px;width:305px;height:279px;background:var(--white);box-shadow:0 2px 10px rgba(0,0,0,.08)}
.avatar{position:absolute;left:95px;top:-58px;width:116px;height:116px;border-radius:50%;border:5px solid var(--white);box-shadow:0 2px 6px rgba(0,0,0,.15)}
.quote .stars{position:absolute;left:0;width:100%;top:100px;text-align:center;color:#f2a900;font-size:16px;letter-spacing:1px}
.quote h4{position:absolute;left:0;width:100%;top:130px;text-align:center;font:700 16px "Roboto",sans-serif;color:var(--ink)}
.quote p{position:absolute;left:24px;width:257px;top:158px;text-align:center;font:400 14px/24px "Roboto",sans-serif;color:var(--text)}
.arrow{position:absolute;width:24px;height:24px;border-radius:50%;border:1.5px solid #888;display:flex;align-items:center;justify-content:center}

/* condo views */
.slide{border-radius:10px;box-shadow:0 4px 14px rgba(0,0,0,.2)}
.round-btn{position:absolute;top:4015px;width:40px;height:40px;border-radius:50%;border:2px solid var(--ink);display:flex;align-items:center;justify-content:center}

/* footer */
.footer{top:4140px;left:0;width:1200px;height:559px}
.footer svg{position:absolute;left:0;top:0}
.fcol{position:absolute;top:196px;color:var(--white)}
.fcol h5{font:700 20px "Roboto",sans-serif;margin-bottom:18px}
.fcol ul{list-style:none;font:400 13px "Roboto",sans-serif}
.fcol li{height:29px;display:flex;align-items:center;gap:10px}
.contact-row{display:flex;align-items:center;gap:14px;height:58px;font:400 14px "Roboto",sans-serif}
.contact-row .ic{width:34px;height:34px;border-radius:50%;background:var(--white);display:flex;align-items:center;justify-content:center;flex:none}
.news p{font:400 13px/26px "Roboto",sans-serif;width:266px}
.news .field{margin-top:12px;width:262px;border-bottom:1px solid var(--white);padding-bottom:8px;font:400 13px "Roboto",sans-serif}
.news .sub{margin-top:28px;width:140px;height:46px;border-radius:23px;background:var(--white);color:var(--black);font:700 16px "Roboto",sans-serif;display:flex;align-items:center;justify-content:center}
.copy-line{top:4622px;left:98px;width:1004px;height:2px;background:#888}
.copyright{top:4651px;left:0;width:1200px;text-align:center;color:var(--white);font:400 14px "Roboto",sans-serif}
</style>
</head>
<body>

<div class="abs topbar">
  <a class="abs cta" href="#">Click here to check our calendar</a>
  <div class="abs social"><span></span><span></span><span></span><span></span></div>
</div>

<header class="abs header">
  <div class="abs brand">Cormant Haven</div>
  <a class="abs nav active" style="left:480px" href="#">Home</a>
  <a class="abs nav" style="left:547px" href="#">About</a>
  <a class="abs nav" style="left:613px" href="#">Things to Do</a>
  <a class="abs nav" style="left:728px" href="#">Attractions</a>
  <a class="abs nav" style="left:828px" href="#">Events</a>
  <a class="abs nav" style="left:903px" href="#">Blog</a>
  <a class="btn-contact abs" href="#">Contact Us</a>
</header>
<nav class="abs subnav">
  <span style="left:117px">Plan Your Trip</span>
  <span style="left:261px">Recommended Travel Agency</span>
  <span style="left:520px">Things to Consider</span>
  <span style="left:699px">Local Services</span>
  <span style="left:846px">Reviews</span>
  <span style="left:950px">Events &amp; Festivals</span>
</nav>

<section class="abs hero">
  <div class="hero-photo" role="img" aria-label="Family on Flagler Beach next to the fishing pier with oceanfront buildings"></div>
  <div class="hero-shade"></div>
  <svg width="1200" height="591" viewBox="0 0 1200 591">
    <path d="M0,436 Q600,620 1200,436 L1200,591 L0,591 Z" fill="#fff"/>
    <path d="M173,509 Q600,680 1030,509 Q600,630 173,509 Z" fill="#1f82c8"/>
  </svg>
  <h1>Stay in Our Flagler Beach<br>Oceanfront Condo</h1>
  <p>Your perfect Flagler Beach getaway — ocean views, modern amenities,<br>and steps from the sand.</p>
  <a class="pill" style="left:343px;width:137px;background:#2187c9" href="#">Book on StayNest</a>
  <a class="pill" style="left:489px;width:139px;background:var(--mint)" href="#">Book on HomeHop</a>
  <a class="pill" style="left:637px;width:219px;background:#1c4c9c" href="#">Book on LeaseLoft</a>
</section>

<h2 class="abs title" style="top:845px">Welcome to Your <b>Flagler Beach Vacation Home</b></h2>
<div class="abs rule" style="top:896px"></div>
<p class="abs welcome-text">Welcome to your coastal retreat, perfectly situated just steps from the beach. This pet-friendly property offers stunning<br>ocean views and the convenience of a short walk to the shoreline, making it ideal for both relaxation and adventure.<br>Whether you're unwinding on the balcony or strolling with your pup along the sand, this getaway blends comfort with an<br>unbeatable location.</p>

<div class="abs bubble" style="left:155px;background:linear-gradient(160deg,#3d9a98 0%,#6fb9a6 50%,#8fc79a 100%)" role="img" aria-label="Beach and pier in teal tones">
  <div class="label">Beach<svg width="16" height="16" viewBox="0 0 16 16"><circle cx="8" cy="8" r="8" fill="#fff"/><path d="M5 8h6M8 5l3 3-3 3" stroke="#3d9a98" stroke-width="1.8" fill="none"/></svg></div>
</div>
<div class="abs bubble" style="left:430px;background:radial-gradient(circle at 50% 45%,#fbf27a 0%,#f1e85a 60%,#e2d84a 100%)" role="img" aria-label="Restaurant interior in yellow tones">
  <div class="label" style="color:#222">Local Restaurants<svg width="16" height="16" viewBox="0 0 16 16"><circle cx="8" cy="8" r="8" fill="#222"/><path d="M5 8h6M8 5l3 3-3 3" stroke="#f1e85a" stroke-width="1.8" fill="none"/></svg></div>
</div>
<div class="abs bubble" style="left:717px;background:linear-gradient(160deg,#4b78ad 0%,#5d84a8 45%,#7e8f96 70%,#44679a 100%)" role="img" aria-label="Aerial view of the coastline and town">
  <div class="label">Attractions<svg width="16" height="16" viewBox="0 0 16 16"><circle cx="8" cy="8" r="8" fill="#fff"/><path d="M5 8h6M8 5l3 3-3 3" stroke="#44679a" stroke-width="1.8" fill="none"/></svg></div>
</div>

<section class="abs why">
  <div class="abs why-photo" role="img" aria-label="Aerial view of the condo neighbourhood beside the beach"></div>
  <h2 class="abs">Why Our Condo Is<br><b>Perfect for Your Stay</b></h2>
  <ul class="abs features">
    <li><svg width="22" height="14" viewBox="0 0 22 14"><path d="M2 1l6 6-6 6M10 1l6 6-6 6" stroke="#1f82c8" stroke-width="3" fill="none"/></svg>Oceanfront balcony with panoramic Atlantic views</li>
    <li><svg width="22" height="14" viewBox="0 0 22 14"><path d="M2 1l6 6-6 6M10 1l6 6-6 6" stroke="#1f82c8" stroke-width="3" fill="none"/></svg>Pet-friendly accommodations for dogs</li>
    <li><svg width="22" height="14" viewBox="0 0 22 14"><path d="M2 1l6 6-6 6M10 1l6 6-6 6" stroke="#1f82c8" stroke-width="3" fill="none"/></svg>Steps from Flagler Beach shoreline</li>
    <li><svg width="22" height="14" viewBox="0 0 22 14"><path d="M2 1l6 6-6 6M10 1l6 6-6 6" stroke="#1f82c8" stroke-width="3" fill="none"/></svg>Fully furnished kitchen and modern appliances</li>
    <li><svg width="22" height="14" viewBox="0 0 22 14"><path d="M2 1l6 6-6 6M10 1l6 6-6 6" stroke="#1f82c8" stroke-width="3" fill="none"/></svg>Spacious living area, bedrooms, and bathrooms</li>
    <li><svg width="22" height="14" viewBox="0 0 22 14"><path d="M2 1l6 6-6 6M10 1l6 6-6 6" stroke="#1f82c8" stroke-width="3" fill="none"/></svg>Free parking and easy access to local shops and restaurants</li>
  </ul>
  <a class="sq" style="left:644px;top:450px;width:153px;background:#13a98f" href="#">Book on StayNest</a>
  <a class="sq" style="left:826px;top:450px;width:159px;background:#2187c9" href="#">Book on HomeHop</a>
  <a class="sq" style="left:644px;top:508px;width:237px;background:#1c4c9c" href="#">Book on LeaseLoft</a>
</section>

<h2 class="abs title" style="top:2206px">Explore Flagler <b>Beach, Florida</b></h2>
<div class="abs rule" style="top:2257px"></div>
<p class="abs explore-text">Flagler Beach is a charming seaside town on Florida's Atlantic coast. Known for its historic fishing pier, scenic A1A highway,<br>family-friendly beaches, and local eateries, it's a peaceful alternative to crowded tourist destinations. Visitors love strolling<br>the pier, enjoying fresh seafood, and exploring nearby parks and nature trails.</p>

<div class="abs card" style="left:110px">
  <div class="shot" style="background:linear-gradient(180deg,#aebfd0 0%,#c5d0d8 45%,#8ea6ad 58%,#d8cdb8 75%,#c9b99c 100%)" role="img" aria-label="Beach shoreline with waves under a cloudy sky"></div>
  <h3>Historic Fishing Pier</h3>
</div>
<div class="abs card" style="left:446px">
  <div class="shot" style="background:linear-gradient(180deg,#4f8fb8 0%,#7fa9c0 25%,#b3a88f 55%,#8f9a86 80%,#6f8a78 100%)" role="img" aria-label="Aerial view of buildings along the A1A highway"></div>
  <h3>Scenic A1A Highway</h3>
</div>
<div class="abs card" style="left:781px">
  <div class="shot" style="background:linear-gradient(180deg,#b9c6d3 0%,#cdd6de 60%,#8d9aa6 85%,#5a5f66 100%)" role="img" aria-label="Paragliders above the pier"></div>
  <h3>Parks and Nature Trails</h3>
</div>

<section class="abs testimonials">
  <h2 class="abs title" style="top:63px">Client <b>Testimonials</b></h2>
  <div class="abs rule" style="top:115px"></div>
  <div class="arrow" style="left:43px;top:349px"><svg width="10" height="10" viewBox="0 0 10 10"><path d="M6 1L2 5l4 4" stroke="#888" stroke-width="1.5" fill="none"/></svg></div>
  <div class="arrow" style="left:1132px;top:349px"><svg width="10" height="10" viewBox="0 0 10 10"><path d="M4 1l4 4-4 4" stroke="#888" stroke-width="1.5" fill="none"/></svg></div>

  <div class="abs quote" style="left:111px">
    <div class="avatar" style="background:linear-gradient(160deg,#d7dde2,#b2764e)" role="img" aria-label="Client portrait"></div>
    <div class="stars">★★★★★</div>
    <h4>John Smith</h4>
    <p>Lorem ipsum dolor sit amet, consectetur adipiscing elit, sed do eiusmod tempor incididunt ut labore et dolore magna aliqua.</p>
  </div>
  <div class="abs quote" style="left:447px">
    <div class="avatar" style="background:linear-gradient(160deg,#dfe5ea,#5f8fb2)" role="img" aria-label="Client portrait"></div>
    <div class="stars">★★★★★</div>
    <h4>John Smith</h4>
    <p>Lorem ipsum dolor sit amet, consectetur adipiscing elit, sed do eiusmod tempor incididunt ut labore et dolore magna aliqua.</p>
  </div>
  <div class="abs quote" style="left:784px">
    <div class="avatar" style="background:linear-gradient(160deg,#4fb3e0,#e6a93a)" role="img" aria-label="Client portrait"></div>
    <div class="stars">★★★★★</div>
    <h4>John Smith</h4>
    <p>Lorem ipsum dolor sit amet, consectetur adipiscing elit, sed do eiusmod tempor incididunt ut labore et dolore magna aliqua.</p>
  </div>
</section>

<h2 class="abs title" style="top:3518px">Explore Our <b>Condo &amp; Views</b></h2>
<div class="abs rule" style="top:3569px"></div>
<div class="abs slide" style="left:113px;top:3645px;width:122px;height:277px;background:linear-gradient(180deg,#c9a983,#b79570)" role="img" aria-label="Dog on the sand"></div>
<div class="abs slide" style="left:232px;top:3619px;width:186px;height:330px;background:linear-gradient(180deg,#7c9cc7 0%,#a9bdd4 45%,#8ca6b0 60%,#c7b89a 100%)" role="img" aria-label="Beach and surf under blue sky"></div>
<div class="abs slide" style="left:760px;top:3619px;width:191px;height:330px;background:linear-gradient(180deg,#3d3a44 0%,#c2762c 40%,#e8a03b 60%,#5d4a3a 100%)" role="img" aria-label="Sunrise over the pier"></div>
<div class="abs slide" style="left:948px;top:3645px;width:141px;height:277px;background:linear-gradient(180deg,#dedcd8,#c7c2bd)" role="img" aria-label="Bright condo bedroom"></div>
<div class="abs slide" style="left:416px;top:3600px;width:344px;height:367px;background:linear-gradient(180deg,#4f86c9 0%,#6b9bd2 45%,#8a9fb4 70%,#6e7a86 100%)" role="img" aria-label="Pelican perched by the ocean"></div>
<div class="round-btn" style="left:528px"><svg width="18" height="18" viewBox="0 0 18 18"><path d="M15 9H3M8 4L3 9l5 5" stroke="#111" stroke-width="2" fill="none"/></svg></div>
<div class="round-btn" style="left:626px"><svg width="18" height="18" viewBox="0 0 18 18"><path d="M3 9h12M10 4l5 5-5 5" stroke="#111" stroke-width="2" fill="none"/></svg></div>

<footer class="abs footer">
  <svg width="1200" height="559" viewBox="0 0 1200 559">
    <path d="M0,180 Q600,40 1200,180 L1200,559 L0,559 Z" fill="#000"/>
    <path d="M165,120 Q600,-10 1035,120 Q600,30 165,120 Z" fill="#1f82c8"/>
  </svg>

  <div class="fcol" style="left:110px">
    <h5>Quick Links</h5>
    <ul>
      <li><svg width="12" height="12" viewBox="0 0 12 12"><path d="M1 6h9M6 2l4 4-4 4" stroke="#fff" stroke-width="2" fill="none"/></svg>Home</li>
      <li><svg width="12" height="12" viewBox="0 0 12 12"><path d="M1 6h9M6 2l4 4-4 4" stroke="#fff" stroke-width="2" fill="none"/></svg>Book Our Condo</li>
      <li><svg width="12" height="12" viewBox="0 0 12 12"><path d="M1 6h9M6 2l4 4-4 4" stroke="#fff" stroke-width="2" fill="none"/></svg>About Flagler</li>
      <li><svg width="12" height="12" viewBox="0 0 12 12"><path d="M1 6h9M6 2l4 4-4 4" stroke="#fff" stroke-width="2" fill="none"/></svg>Things to Do</li>
      <li><svg width="12" height="12" viewBox="0 0 12 12"><path d="M1 6h9M6 2l4 4-4 4" stroke="#fff" stroke-width="2" fill="none"/></svg>Attractions</li>
      <li><svg width="12" height="12" viewBox="0 0 12 12"><path d="M1 6h9M6 2l4 4-4 4" stroke="#fff" stroke-width="2" fill="none"/></svg>Events &amp; Festivals</li>
    </ul>
  </div>
  <div class="fcol" style="left:288px">
    <h5>Other Links</h5>
    <ul>
      <li><svg width="12" height="12" viewBox="0 0 12 12"><path d="M1 6h9M6 2l4 4-4 4" stroke="#fff" stroke-width="2" fill="none"/></svg>Plan Your Trip</li>
      <li><svg width="12" height="12" viewBox="0 0 12 12"><path d="M1 6h9M6 2l4 4-4 4" stroke="#fff" stroke-width="2" fill="none"/></svg>Recommended Travel Agency</li>
      <li><svg width="12" height="12" viewBox="0 0 12 12"><path d="M1 6h9M6 2l4 4-4 4" stroke="#fff" stroke-width="2" fill="none"/></svg>Things to Consider</li>
      <li><svg width="12" height="12" viewBox="0 0 12 12"><path d="M1 6h9M6 2l4 4-4 4" stroke="#fff" stroke-width="2" fill="none"/></svg>Local Services</li>
      <li><svg width="12" height="12" viewBox="0 0 12 12"><path d="M1 6h9M6 2l4 4-4 4" stroke="#fff" stroke-width="2" fill="none"/></svg>Blog</li>
      <li><svg width="12" height="12" viewBox="0 0 12 12"><path d="M1 6h9M6 2l4 4-4 4" stroke="#fff" stroke-width="2" fill="none"/></svg>Reviews</li>
    </ul>
  </div>
  <div class="fcol" style="left:549px">
    <h5>Contact Us</h5>
    <div class="contact-row"><span class="ic"><svg width="14" height="16" viewBox="0 0 14 16"><path d="M7 15s5-5.5 5-9A5 5 0 0 0 2 6c0 3.5 5 9 5 9z" fill="#000"/><circle cx="7" cy="6" r="2" fill="#fff"/></svg></span>Company Name,United State.</div>
    <div class="contact-row"><span class="ic"><svg width="16" height="12" viewBox="0 0 16 12"><rect x="1" y="1" width="14" height="10" rx="1" fill="#000"/><path d="M1 1l7 6 7-6" stroke="#fff" stroke-width="1.4" fill="none"/></svg></span>info@companyname.in</div>
    <div class="contact-row"><span class="ic"><svg width="14" height="14" viewBox="0 0 14 14"><path d="M3 1l2.5 3-1.5 1.5a8 8 0 0 0 4.5 4.5L10 8.5 13 11l-1.5 2C6 13 1 8 1 2.5z" fill="#000"/></svg></span>+1888 8888 8888</div>
  </div>
  <div class="fcol news" style="left:828px">
    <h5>Sign Up Our Newsletter</h5>
    <p>Lorem ipsum dolor sit amet,consectetur adipiscing elit,adipiscing elit.</p>
    <div class="field">Email</div>
    <div class="sub">Subscribe</div>
  </div>
</footer>
<div class="abs copy-line"></div>
<div class="abs copyright">Copyrights@2025.Company Name.All Rights Reserved</div>

</body>
</html>
```